New Graphic Design Project / Email signiture and Letterhead

I would like a new SIMPLE but high end quality modern/heavy industrial design for an email Signiture and letter head that incorporates product photos or illustrations of our products to show our customers our range of products and also show our head office in Perth Western Australia and also our Australian and international reseller locations.
in my present email signature you would see that I have other company logos these companies are old partners of ours but some are no longer so I would like to have the option to add and change them if things change in the future.
for ideas Our main products are as follows
Composite Hose
Convoluted hose
Metal expansion joints
Fabric expansion joints
Rubber Expansion joints
Please see our website for ideas and our product photos.
www.brovantec.com.au
if you need any further information please let me know
i have attached our old email signiture for reference.
Declan

Target Market(s)

Oil and Gas / Mining / Petroleum and Chemical Refineries, high end engineering

Requirements
Must have
• pictures / photos of our core products and our company capabilities to show our existing and new customers what we can do.
in the email signature - links to company face book and LinkedIn, our website
I would like to have spaces for my company partners logos and need the final file to be in a format for me to change and update all details
All so our Font is Conthrax SB
Nice to have
• the email signature, I would like this to have all the required information ( as per attached present email signature ) but also be informative / marketing to show customers what we do if possible.
the letter head can be based from the same but simple with or without product photos

```html
<!DOCTYPE html>
<html lang="en">
<head>
<meta charset="utf-8">
<title>Brovantec Letterhead</title>
<link rel="stylesheet" href="https://fonts.googleapis.com/css2?family=Open+Sans:wght@400;600;700&display=swap">
<style>
:root{
  --bg-top:#a8a9ac;
  --bg-bottom:#929294;
  --paper:#ffffff;
  --ink:#1d1d1f;
  --ink-soft:#333336;
  --band-grey:#5b5b5d;
  --band-dark:#1d1d1f;
  --faint:#f4f5f7;
}
*{margin:0;padding:0;box-sizing:border-box}
html,body{width:1200px;height:1102px;overflow:hidden}
body{
  position:relative;
  background:linear-gradient(180deg,var(--bg-top) 0%,var(--bg-bottom) 100%);
  font-family:"Open Sans",Arial,sans-serif;
  color:var(--ink);
}
.letterhead{
  position:absolute;top:257px;width:420px;height:588px;
  background:var(--paper);overflow:hidden;
}
.letterhead--banded{left:150px}
.letterhead--plain{left:630px}
.side-band{position:absolute;left:0;top:0;width:32px;height:100%;background:var(--band-dark)}
.side-band::before{content:"";position:absolute;left:0;top:0;width:100%;height:189px;background:var(--band-grey)}
.brand{position:absolute;left:50px;top:65px;display:flex;align-items:center;gap:7px}
.brand-dot{width:26px;height:26px;border:2.5px solid var(--ink-soft);border-radius:50%}
.brand-name{font-weight:700;font-size:13px;letter-spacing:.6px;color:var(--ink)}
.watermark{position:absolute;left:65px;top:138px;width:310px;height:310px;border:23px solid var(--faint);border-radius:50%}
.footer-rule{position:absolute;left:54px;top:519px;width:313px;height:2px;background:var(--ink)}
.footer-street{position:absolute;left:54px;top:526px;font-size:7.2px;font-weight:600;color:var(--ink)}
.contact{position:absolute;display:flex;align-items:center;gap:6px;font-size:6.4px;line-height:7.8px;color:var(--ink-soft)}
.contact-icon{width:13px;height:13px;background:var(--ink);border-radius:2px;display:flex;align-items:center;justify-content:center;flex:none}
.contact--phone{left:54px;top:539px}
.contact--mail{left:127px;top:539px}
.contact--place{left:54px;top:559px}
.contact--place .contact-icon{margin-right:3px}
.product{position:absolute;border-radius:6px}
.product--composite{left:296px;top:526px;width:35px;height:19px;background:linear-gradient(90deg,#2f4f86,#6b86b8)}
.product--convoluted{left:335px;top:527px;width:32px;height:17px;background:linear-gradient(90deg,#9a9ca0,#d0d1d4)}
.product--metal{left:280px;top:552px;width:24px;height:22px;background:linear-gradient(90deg,#8d8f93,#c9cacc)}
.product--fabric{left:312px;top:552px;width:19px;height:22px;background:linear-gradient(90deg,#2a2b2e,#6e7075)}
.product--rubber{left:342px;top:553px;width:22px;height:20px;background:linear-gradient(90deg,#1e2027,#4a5264)}
</style>
</head>
<body>

<section class="letterhead letterhead--banded">
  <div class="side-band"></div>
  <div class="brand"><span class="brand-dot"></span><span class="brand-name">BROVANTEC</span></div>
  <div class="watermark"></div>
  <div class="footer-rule"></div>
  <p class="footer-street">Your Street Address Here United State, 54789</p>
  <div class="contact contact--phone">
    <span class="contact-icon"><svg width="8" height="8" viewBox="0 0 24 24"><path fill="#fff" d="M6.6 10.8a15 15 0 0 0 6.6 6.6l2.2-2.2c.3-.3.7-.4 1-.2 1.1.4 2.3.6 3.6.6.6 0 1 .4 1 1V20c0 .6-.4 1-1 1A17 17 0 0 1 3 4c0-.6.4-1 1-1h3.5c.6 0 1 .4 1 1 0 1.3.2 2.5.6 3.6.1.3 0 .7-.2 1z"/></svg></span>
    <span>+614 40 555 218<br>+618 95 550 142</span>
  </div>
  <div class="contact contact--mail">
    <span class="contact-icon"><svg width="9" height="7" viewBox="0 0 18 14"><rect x="1" y="1" width="16" height="12" fill="none" stroke="#fff" stroke-width="1.6"/><path d="M1 1l8 7 8-7" fill="none" stroke="#fff" stroke-width="1.6"/></svg></span>
    <span>declan@brovantec.com.au<br>www.brovantec.com.au</span>
  </div>
  <div class="contact contact--place">
    <span class="contact-icon"><svg width="7" height="9" viewBox="0 0 14 18"><path fill="#fff" d="M7 0a7 7 0 0 0-7 7c0 5 7 11 7 11s7-6 7-11a7 7 0 0 0-7-7zm0 9.5A2.5 2.5 0 1 1 7 4.5a2.5 2.5 0 0 1 0 5z"/></svg></span>
    <span>88 Quarry Lane<br>Welshpool, WA 6106</span>
  </div>
  <div class="product product--composite" role="img" aria-label="Photo of blue composite hose coil"></div>
  <div class="product product--convoluted" role="img" aria-label="Photo of stainless convoluted hose"></div>
  <div class="product product--metal" role="img" aria-label="Photo of metal expansion joint"></div>
  <div class="product product--fabric" role="img" aria-label="Photo of fabric expansion joint"></div>
  <div class="product product--rubber" role="img" aria-label="Photo of rubber expansion joint"></div>
</section>

<section class="letterhead letterhead--plain">
  <div class="brand"><span class="brand-dot"></span><span class="brand-name">BROVANTEC</span></div>
  <div class="watermark"></div>
  <div class="footer-rule"></div>
  <p class="footer-street">Your Street Address Here United State, 54789</p>
  <div class="contact contact--phone">
    <span class="contact-icon"><svg width="8" height="8" viewBox="0 0 24 24"><path fill="#fff" d="M6.6 10.8a15 15 0 0 0 6.6 6.6l2.2-2.2c.3-.3.7-.4 1-.2 1.1.4 2.3.6 3.6.6.6 0 1 .4 1 1V20c0 .6-.4 1-1 1A17 17 0 0 1 3 4c0-.6.4-1 1-1h3.5c.6 0 1 .4 1 1 0 1.3.2 2.5.6 3.6.1.3 0 .7-.2 1z"/></svg></span>
    <span>+614 40 555 218<br>+618 95 550 142</span>
  </div>
  <div class="contact contact--mail">
    <span class="contact-icon"><svg width="9" height="7" viewBox="0 0 18 14"><rect x="1" y="1" width="16" height="12" fill="none" stroke="#fff" stroke-width="1.6"/><path d="M1 1l8 7 8-7" fill="none" stroke="#fff" stroke-width="1.6"/></svg></span>
    <span>declan@brovantec.com.au<br>www.brovantec.com.au</span>
  </div>
  <div class="contact contact--place">
    <span class="contact-icon"><svg width="7" height="9" viewBox="0 0 14 18"><path fill="#fff" d="M7 0a7 7 0 0 0-7 7c0 5 7 11 7 11s7-6 7-11a7 7 0 0 0-7-7zm0 9.5A2.5 2.5 0 1 1 7 4.5a2.5 2.5 0 0 1 0 5z"/></svg></span>
    <span>88 Quarry Lane<br>Welshpool, WA 6106</span>
  </div>
  <div class="product product--composite" role="img" aria-label="Photo of blue composite hose coil"></div>
  <div class="product product--convoluted" role="img" aria-label="Photo of stainless convoluted hose"></div>
  <div class="product product--metal" role="img" aria-label="Photo of metal expansion joint"></div>
  <div class="product product--fabric" role="img" aria-label="Photo of fabric expansion joint"></div>
  <div class="product product--rubber" role="img" aria-label="Photo of rubber expansion joint"></div>
</section>

</body>
</html>
```